Tin Lark Ledger Series 1 Volume 1

I am looking for someone to make me a book cover, I want something catchy but classy.

The title of the book is; Tin Lark Ledger
Series 1 Volume 1

Colors should be: Red, White, Black and Grey

```html
<!DOCTYPE html>
<html lang="en">
<head>
<meta charset="utf-8">
<title>Tin Lark Ledger — Series 1 Volume 1</title>
<link rel="stylesheet" href="https://fonts.googleapis.com/css2?family=Oswald:wght@400;500;600&display=swap">
<style>
  :root {
    --stage: #000000;
    --paper-top: #ffffff;
    --paper-bottom: #e9e9e9;
    --ink: #111111;
    --red: #e3161e;
    --white: #ffffff;
    --art-red: #c8141b;
    --art-dark: #2b2b2b;
  }
  * { margin: 0; padding: 0; box-sizing: border-box; }
  html, body {
    width: 1200px;
    height: 843px;
    overflow: hidden;
    background: var(--stage);
  }
  .canvas {
    position: relative;
    width: 1200px;
    height: 843px;
    background: var(--stage);
  }
  .cover {
    position: absolute;
    left: 357px;
    top: 67px;
    width: 496px;
    height: 704px;
    background: linear-gradient(180deg, var(--paper-top) 0%, var(--paper-bottom) 100%);
    font-family: "Oswald", "Arial Narrow", sans-serif;
    text-align: center;
  }
  .volume-label {
    position: absolute;
    top: 14px;
    left: 0;
    right: 0;
    font-size: 22px;
    font-weight: 500;
    letter-spacing: 15px;
    text-indent: 15px;
    color: var(--ink);
  }
  .volume-label .num { color: var(--red); }
  .title {
    position: absolute;
    top: 64px;
    left: 0;
    right: 0;
    font-weight: 500;
    line-height: 1;
  }
  .title-top {
    display: block;
    font-size: 70px;
    letter-spacing: 12px;
    text-indent: 12px;
    color: var(--ink);
  }
  .title-bottom {
    display: block;
    margin-top: 7px;
    font-size: 93px;
    letter-spacing: 18px;
    text-indent: 18px;
    color: var(--red);
  }
  .series-tag {
    position: absolute;
    top: 248px;
    left: 171px;
    width: 155px;
    height: 28px;
    border: 2px solid var(--red);
    font-size: 17px;
    font-weight: 500;
    letter-spacing: 5px;
    text-indent: 5px;
    line-height: 24px;
    color: var(--ink);
  }
  .series-tag .num { color: var(--red); }
  .cover-art {
    position: absolute;
    top: 309px;
    left: 21px;
    width: 459px;
    height: 304px;
  }
  .author-band {
    position: absolute;
    left: 0;
    right: 0;
    top: 649px;
    height: 36px;
    background: var(--red);
    color: var(--white);
    font-size: 22px;
    font-weight: 400;
    letter-spacing: 9px;
    text-indent: 9px;
    line-height: 36px;
  }
</style>
</head>
<body>
<main class="canvas">
  <article class="cover">
    <p class="volume-label">VOLUME-<span class="num">1</span></p>
    <h1 class="title">
      <span class="title-top">TIN LARK</span>
      <span class="title-bottom">LEDGER</span>
    </h1>
    <p class="series-tag">SERIES-<span class="num">1</span></p>
    <svg class="cover-art" viewBox="0 0 459 304" role="img" aria-label="Photo of an open laptop whose screen shows a row of red ring binders, one binder sliding out onto the keyboard">
      <defs>
        <linearGradient id="art-tone" x1="0" y1="0" x2="0" y2="1">
          <stop offset="0" stop-color="var(--art-red)"/>
          <stop offset="1" stop-color="var(--art-dark)"/>
        </linearGradient>
      </defs>
      <rect x="0" y="0" width="459" height="304" fill="url(#art-tone)"/>
    </svg>
    <p class="author-band">MAREN ELISE HOLLOWAY</p>
  </article>
</main>
</body>
</html>
```